Convert MS Word FIle into Magazine with a new Cover Design (Indesign)

Essentially, I need help to transform a simple MS Word document into a magazine. We are an alternative health supplier (Thorne flower remedies) looking to appeal to target market of women aged 25-45, who are interested in holistic healing/nwaw age/natural remedies. The magazine should have art nouveau or art deco touches, eluding to when Thorne flower essences were first discovered. I have some pictures in the document you must use, but feel free to add in relevant pictures and graphics that you see fit - such as flowers or pictures of essential oils etc.

Project is completed now! Thank you!

```html
<!DOCTYPE html>
<html lang="en">
<head>
<meta charset="utf-8">
<title>Thorne Flower Remedies – Introduction spread</title>
<link rel="stylesheet" href="https://fonts.googleapis.com/css2?family=Quicksand:wght@400;600;700&family=Sofia&display=swap">
<style>
  :root {
    --backdrop: #e6e6e4;
    --paper: #ffffff;
    --rose: #c4578a;
    --rose-deep: #a8466f;
    --rose-soft: #d98fb0;
    --moss: #5f7a22;
    --ink: #4a4a4a;
    --ink-light: #ffffff;
  }
  * { box-sizing: border-box; margin: 0; padding: 0; }
  html, body {
    width: 1200px; height: 800px; overflow: hidden;
    background: var(--backdrop);
  }
  .spread {
    position: absolute; left: 90px; top: 40px;
    width: 1020px; height: 720px;
    display: flex;
    box-shadow: 0 4px 18px rgba(0,0,0,.12);
  }
  .page {
    position: relative; width: 510px; height: 720px;
    background: var(--paper); overflow: hidden;
    font-family: "Quicksand", sans-serif;
  }
  .page--left { background: linear-gradient(to left, #ececec 0, var(--paper) 24px); }
  .page--right { background: linear-gradient(to right, #e4e4e4 0, var(--paper) 30px); }

  /* Introduction panel */
  .intro-panel {
    position: absolute; left: 0; top: 0; width: 510px; height: 470px;
    background: linear-gradient(160deg, var(--rose-soft) 0%, var(--rose) 55%, var(--rose-deep) 100%);
    padding: 28px 36px 0 40px;
    color: var(--ink-light);
  }
  .intro-panel__flora {
    position: absolute; right: 0; top: 0; width: 260px; height: 470px;
    background: radial-gradient(ellipse at 60% 40%, rgba(255,255,255,.16), rgba(255,255,255,0) 70%);
  }
  .page-title {
    font-family: "Sofia", cursive;
    font-weight: 400;
    font-size: 25px;
    margin-bottom: 20px;
    position: relative;
  }
  .intro-panel .page-title { color: var(--ink-light); }
  .intro-body { position: relative; }
  .intro-body p {
    font-size: 9.6px; line-height: 1.55; margin-bottom: 11px;
  }

  /* frame lines */
  .rule { position: absolute; background: var(--rose); }
  .rule--h { height: 1px; }
  .rule--v { width: 1px; }

  /* side tabs */
  .side-tab {
    position: absolute; width: 30px;
    background: var(--rose);
    display: flex; align-items: center; justify-content: center;
  }
  .side-tab span {
    writing-mode: vertical-rl;
    font-family: "Sofia", cursive;
    font-size: 12px; color: var(--ink-light);
  }
  .page--left .side-tab span { transform: rotate(180deg); }

  /* brand block */
  .brand-box {
    position: absolute; left: 40px; top: 470px; width: 210px; height: 125px;
    border: 1px solid var(--rose);
    display: flex; align-items: center; justify-content: center; gap: 8px;
  }
  .brand-box__dot { width: 10px; height: 10px; border-radius: 50%; background: var(--moss); }
  .brand-box__name {
    font-family: "Quicksand", sans-serif; font-weight: 700;
    font-size: 17px; color: var(--moss); letter-spacing: .5px;
  }

  /* folios */
  .folio {
    position: absolute; height: 40px;
    background: var(--moss);
    color: var(--ink-light);
    font-size: 11px; font-weight: 600;
    display: flex; align-items: center; justify-content: center;
  }

  /* imprint */
  .imprint {
    position: absolute; left: 268px; top: 484px; width: 220px;
    color: var(--ink); font-size: 7.6px; line-height: 1.5;
  }
  .imprint__owner { font-weight: 700; font-size: 8.4px; margin-bottom: 8px; }
  .imprint p { margin-bottom: 8px; }

  /* contents page */
  .contents-title {
    position: absolute; left: 40px; top: 40px;
    color: var(--rose);
  }
</style>
</head>
<body>
  <main class="spread">
    <section class="page page--left">
      <div class="intro-panel">
        <div class="intro-panel__flora" role="img" aria-label="Faint wildflower stems in pale pink behind the text"></div>
        <h1 class="page-title">Introduction</h1>
        <div class="intro-body">
          <p>Thorne Flower Remedies were developed by Dr. Thorne in the early part of the 20th century to gently address emotional imbalance. He believed that healing the mind was the first step toward healing the body, and that nature offered everything needed.</p>
          <p>Alternative therapies make no distinction between body and mind. Each remedy is prepared from the blossoms of wild plants and trees, preserved in water and brandy, and taken a few drops at a time to restore calm, courage and balance through the day.</p>
          <p>Aromatherapy works in a similar way, using the scent of pure essential oils to lift the mood and soothe the senses.</p>
          <p>The primary aim of this book is to help readers understand the remedies and choose the right blend for their own needs. By learning how each flower relates to a state of mind, you can build a simple daily ritual of care.</p>
          <p>In the chapters that follow, we look at each of the thirty-eight essences in turn, along with practical tips on dosage, blending and pairing them with oils, so that you feel ready to start your own journey.</p>
        </div>
      </div>

      <div class="side-tab" style="left:0; top:395px; height:170px;"><span>Introduction</span></div>

      <div class="brand-box">
        <span class="brand-box__dot"></span>
        <span class="brand-box__name">Hollowmere Remedies</span>
      </div>
      <div class="folio" style="left:40px; top:595px; width:210px;">3</div>

      <div class="imprint">
        <p class="imprint__owner">© 2014 Hollowmere Remedies Pte Ltd</p>
        <p>No part of this publication may be reproduced, stored in a retrieval system or transmitted in any form or by any means without the prior written permission of the publisher. Requests should be addressed to Hollowmere Remedies, 12 Fern Lane, Unit 04-05, Singapore 100245, or hello@hollowmere.com.</p>
        <p>The publisher makes no representation or warranty as to the contents of this book. The remedies described are for general wellbeing only, and a qualified practitioner should be consulted before using any remedy or technique shown in this workbook.</p>
      </div>

      <div class="rule rule--v" style="left:30px; top:470px; height:250px;"></div>
      <div class="rule rule--v" style="left:258px; top:470px; height:190px;"></div>
      <div class="rule rule--h" style="left:30px; top:660px; width:480px;"></div>
    </section>

    <section class="page page--right">
      <h2 class="page-title contents-title">Table of Contents</h2>

      <div class="rule rule--v" style="left:480px; top:290px; height:430px;"></div>
      <div class="rule rule--h" style="left:0; top:640px; width:480px;"></div>
      <div class="rule rule--v" style="left:200px; top:640px; height:80px;"></div>

      <div class="folio" style="left:200px; top:640px; width:245px;">4</div>
      <div class="side-tab" style="left:448px; top:560px; height:160px;"><span>Table of Contents</span></div>
    </section>
  </main>
</body>
</html>
```